Fire Hydrant Repair Parts Flyer

We need a flyer advertising both fire hydrant parts and the manufacturers that we are stocking. Our company is Coastal Flowline Supply and we are a parts distributor who sells directly to contractors. I have attached an example flyer that advertises some other parts we stock. We don't want it to look exactly like the old flyer, but we would like it to be structured similarly. I have also attached a background image for the flyer as well as some pictures of the parts we are stocking. I have also attached pictures of the manufacturer logos that we are stocking. We are trying to convey the parts that we are stocking which are: "Traffic Repair Kits", "Main Valve Repair Kits", "Extension Kits", "Replacement Caps & Gaskets", "Replacement Nozzles", Adjustable Hydrant Wrenches", "Hydrant Diffusers", & "Hydrant Oil". I have attached pictures of some of these items that we would like placed on the flyer. Let me know if you have any questions at all.

```html
<!DOCTYPE html>
<html lang="en">
<head>
<meta charset="utf-8">
<title>Fire Hydrant Repair Parts &amp; Accessories</title>
<link rel="stylesheet" href="https://fonts.googleapis.com/css2?family=Anton&family=Montserrat:wght@500;600;700&display=swap">
<style>
  :root {
    --brand-blue: #3a4fa8;
    --brand-navy: #2c3f9e;
    --brand-pink: #d6245c;
    --brand-magenta: #8a3f95;
    --paper: #f6f6f8;
    --ink: #2a2a33;
    --white: #ffffff;
    --line: #d4d4da;
  }
  * { margin: 0; padding: 0; box-sizing: border-box; }
  html, body { width: 1042px; height: 1200px; overflow: hidden; }
  body { background: var(--paper); font-family: "Montserrat", sans-serif; color: var(--ink); }
  .flyer { position: relative; width: 1042px; height: 1200px; overflow: hidden; background: var(--paper); }
  .flyer__art { position: absolute; inset: 0; width: 1042px; height: 1200px; }

  .headline { position: absolute; top: 36px; left: 0; width: 100%; text-align: center; color: var(--white); }
  .headline__title {
    font-family: "Anton", sans-serif; font-weight: 400; font-size: 82px; line-height: 1;
    letter-spacing: 1px; text-shadow: 3px 3px 0 rgba(30,20,60,.55);
    transform: scaleX(1.32); transform-origin: center;
  }
  .headline__sub {
    margin-top: 10px; font-family: "Montserrat", sans-serif; font-weight: 700; font-size: 36px; letter-spacing: 1px;
    transform: scaleX(1.18); transform-origin: center;
  }

  .parts-list { position: absolute; top: 781px; list-style: none; }
  .parts-list--left { left: 55px; }
  .parts-list--right { left: 606px; }
  .parts-list li { display: flex; align-items: center; gap: 11px; height: 31px; font-weight: 500; font-size: 22px; }
  .parts-list svg { width: 12px; height: 12px; flex: none; }

  .products { position: absolute; top: 926px; left: 0; width: 100%; }
  .product {
    position: absolute; width: 118px; height: 112px; border-radius: 50%;
    border: 3px solid var(--brand-magenta); background: var(--white);
  }
  .product__photo { position: absolute; inset: 10px; border-radius: 50%; }

  .makers { position: absolute; top: 1064px; left: 0; width: 100%; }
  .maker {
    position: absolute; width: 140px; height: 48px; background: var(--white);
    border: 1px solid var(--line); display: flex; align-items: center; justify-content: center;
    font-family: "Montserrat", sans-serif; font-weight: 700; font-size: 13px; color: var(--ink);
  }

  .footer { position: absolute; left: 0; top: 1142px; width: 100%; height: 58px; color: var(--white); font-size: 15px; }
  .footer__phone { position: absolute; left: 51px; top: 19px; display: flex; align-items: center; gap: 7px; font-weight: 500; }
  .footer__phone b, .footer__web b { font-weight: 700; }
  .footer__brand {
    position: absolute; left: 0; width: 100%; top: 14px; text-align: center;
    font-weight: 600; font-size: 20px; color: var(--brand-navy);
  }
  .footer__web { position: absolute; left: 740px; top: 19px; display: flex; align-items: center; gap: 7px; font-weight: 500; }
  .footer svg { width: 16px; height: 16px; }
</style>
</head>
<body>
<main class="flyer">
  <svg class="flyer__art" viewBox="0 0 1042 1200" aria-hidden="true">
    <defs>
      <linearGradient id="brandSweep" x1="0" y1="0" x2="1" y2="0">
        <stop offset="0" stop-color="#3a52a8"/>
        <stop offset=".5" stop-color="#7a3f96"/>
        <stop offset="1" stop-color="#d3245e"/>
      </linearGradient>
      <linearGradient id="pinkBand" x1="0" y1="0" x2="1" y2="0">
        <stop offset="0" stop-color="#e01e52"/>
        <stop offset="1" stop-color="#c51e5a"/>
      </linearGradient>
      <linearGradient id="blueBand" x1="0" y1="0" x2="1" y2="0">
        <stop offset="0" stop-color="#2b3f9f"/>
        <stop offset="1" stop-color="#3b50ab"/>
      </linearGradient>
      <linearGradient id="footerLeft" x1="0" y1="0" x2="1" y2="0">
        <stop offset="0" stop-color="#3b52a8"/>
        <stop offset="1" stop-color="#5b4aa3"/>
      </linearGradient>
      <linearGradient id="footerRight" x1="0" y1="0" x2="1" y2="0">
        <stop offset="0" stop-color="#8a3f95"/>
        <stop offset="1" stop-color="#e0245a"/>
      </linearGradient>
    </defs>
    <rect x="0" y="0" width="1042" height="580" fill="url(#brandSweep)"/>
    <path d="M0,395 C200,170 600,110 1042,245 L1042,285 C600,190 200,260 0,470 Z" fill="url(#pinkBand)"/>
    <path d="M0,680 C350,800 800,790 1042,560 L1042,1200 L0,1200 Z" fill="var(--paper)"/>
    <path d="M0,660 C400,760 800,700 1042,478 L1042,560 C800,790 350,800 0,680 Z" fill="url(#blueBand)"/>
    <path d="M0,1142 L333,1142 L377,1200 L0,1200 Z" fill="url(#footerLeft)"/>
    <path d="M1042,1142 L711,1142 L663,1200 L1042,1200 Z" fill="url(#footerRight)"/>
  </svg>

  <svg class="flyer__art" viewBox="0 0 1042 1200" role="img" aria-label="Photo of a red fire hydrant on a grass verge, flushing a wide jet of water across the street">
    <defs>
      <linearGradient id="hydrantPhoto" x1="0" y1="0" x2="1" y2="1">
        <stop offset="0" stop-color="#6f9a4a"/>
        <stop offset=".35" stop-color="#8e9299"/>
        <stop offset=".7" stop-color="#dfe2e6"/>
        <stop offset="1" stop-color="#c9ccd2"/>
      </linearGradient>
    </defs>
    <path d="M0,470 C200,260 600,190 1042,285 L1042,478 C800,700 400,760 0,660 Z" fill="url(#hydrantPhoto)"/>
    <path d="M0,470 C200,260 600,190 1042,285" fill="none" stroke="var(--white)" stroke-width="6"/>
    <path d="M0,660 C400,760 800,700 1042,478" fill="none" stroke="var(--white)" stroke-width="4"/>
  </svg>

  <header class="headline">
    <h1 class="headline__title">FIRE HYDRANT REPAIR</h1>
    <p class="headline__sub">PARTS &amp; ACCESSORIES</p>
  </header>

  <ul class="parts-list parts-list--left">
    <li><svg viewBox="0 0 12 12"><circle cx="6" cy="6" r="6" fill="var(--brand-pink)"/><path d="M3.2 6.2 L5.2 8 L8.8 4" stroke="var(--brand-navy)" stroke-width="1.8" fill="none"/></svg><span>Traffic Repair Kits</span></li>
    <li><svg viewBox="0 0 12 12"><circle cx="6" cy="6" r="6" fill="var(--brand-pink)"/><path d="M3.2 6.2 L5.2 8 L8.8 4" stroke="var(--brand-navy)" stroke-width="1.8" fill="none"/></svg><span>Main Valve Repair Kits</span></li>
    <li><svg viewBox="0 0 12 12"><circle cx="6" cy="6" r="6" fill="var(--brand-pink)"/><path d="M3.2 6.2 L5.2 8 L8.8 4" stroke="var(--brand-navy)" stroke-width="1.8" fill="none"/></svg><span>Extension Kits</span></li>
    <li><svg viewBox="0 0 12 12"><circle cx="6" cy="6" r="6" fill="var(--brand-pink)"/><path d="M3.2 6.2 L5.2 8 L8.8 4" stroke="var(--brand-navy)" stroke-width="1.8" fill="none"/></svg><span>Replacement Caps &amp; Gaskets</span></li>
  </ul>
  <ul class="parts-list parts-list--right">
    <li><svg viewBox="0 0 12 12"><circle cx="6" cy="6" r="6" fill="var(--brand-pink)"/><path d="M3.2 6.2 L5.2 8 L8.8 4" stroke="var(--brand-navy)" stroke-width="1.8" fill="none"/></svg><span>Replacement Nozzles</span></li>
    <li><svg viewBox="0 0 12 12"><circle cx="6" cy="6" r="6" fill="var(--brand-pink)"/><path d="M3.2 6.2 L5.2 8 L8.8 4" stroke="var(--brand-navy)" stroke-width="1.8" fill="none"/></svg><span>Adjustable Hydrant Wrenches</span></li>
    <li><svg viewBox="0 0 12 12"><circle cx="6" cy="6" r="6" fill="var(--brand-pink)"/><path d="M3.2 6.2 L5.2 8 L8.8 4" stroke="var(--brand-navy)" stroke-width="1.8" fill="none"/></svg><span>Hydrant Diffusers</span></li>
    <li><svg viewBox="0 0 12 12"><circle cx="6" cy="6" r="6" fill="var(--brand-pink)"/><path d="M3.2 6.2 L5.2 8 L8.8 4" stroke="var(--brand-navy)" stroke-width="1.8" fill="none"/></svg><span>Hydrant Oil</span></li>
  </ul>

  <section class="products">
    <div class="product" style="left:58px"><div class="product__photo" role="img" aria-label="Red replacement hydrant cap with chain" style="background:radial-gradient(circle at 50% 40%, #e35a5a 0 22%, #d7d9de 45%, #ffffff 70%)"></div></div>
    <div class="product" style="left:215px"><div class="product__photo" role="img" aria-label="Yellow hydrant diffuser with pressure gauge" style="background:radial-gradient(circle at 45% 50%, #f2b21c 0 25%, #c7c9ce 45%, #ffffff 70%)"></div></div>
    <div class="product" style="left:371px"><div class="product__photo" role="img" aria-label="Traffic repair kit with flange and bolts" style="background:radial-gradient(circle at 50% 45%, #3a3a3f 0 25%, #b5b8be 48%, #ffffff 72%)"></div></div>
    <div class="product" style="left:526px"><div class="product__photo" role="img" aria-label="Hydrant extension kit with barrel section" style="background:radial-gradient(circle at 50% 40%, #2f2f34 0 24%, #b0b3ba 48%, #ffffff 72%)"></div></div>
    <div class="product" style="left:682px"><div class="product__photo" role="img" aria-label="Bottle of hydrant oil" style="background:radial-gradient(ellipse 30% 50% at 50% 50%, #e9e9ec 0 60%, #ffffff 100%)"></div></div>
    <div class="product" style="left:838px"><div class="product__photo" role="img" aria-label="Adjustable hydrant wrench" style="background:radial-gradient(circle at 50% 50%, #aeb2b9 0 18%, #e6e7ea 40%, #ffffff 70%)"></div></div>
  </section>

  <section class="makers">
    <div class="maker" style="left:51px">Harbor Flow</div>
    <div class="maker" style="left:205px">Brennan</div>
    <div class="maker" style="left:360px">Kestrel Valve</div>
    <div class="maker" style="left:515px">Summit Pipe</div>
    <div class="maker" style="left:669px">Ridgeline Valve</div>
    <div class="maker" style="left:824px">Granite Valve Co.</div>
  </section>

  <footer class="footer">
    <p class="footer__phone">
      <svg viewBox="0 0 16 16"><circle cx="8" cy="8" r="7" fill="none" stroke="currentColor" stroke-width="1.2"/><path d="M5.3 4.6 L6.6 4.4 L7.2 6.2 L6.3 6.9 C6.8 8 7.6 8.9 8.8 9.5 L9.6 8.7 L11.3 9.4 L11.1 10.7 C8 11 5 8 5.3 4.6 Z" fill="currentColor"/></svg>
      <span>Call Us Today : <b>(800) 555-0142</b></span>
    </p>
    <p class="footer__brand">Coastal Flowline Supply</p>
    <p class="footer__web">
      <svg viewBox="0 0 16 16" fill="none" stroke="currentColor" stroke-width="1.1"><circle cx="8" cy="8" r="7"/><circle cx="8" cy="8" r="4.5"/><ellipse cx="8" cy="8" rx="2" ry="4.5"/><path d="M3.5 8 H12.5"/></svg>
      <span>www.<b>flowlinesupply</b>.com</span>
    </p>
  </footer>
</main>
</body>
</html>
```